Redesign cement bags for leading cement producer in south east asia

We are from Larkfield cement and would like to redesign our bag to relaunch the product line. Our bags are made of high quality PP woven sack. We are one of the leading cement producers and we want our bags to have a Larkfield classy look on each visible side when it is loading in a truck or stacking on a pallet.

Thank you for interesting in this project. Good luck.

Project Deadline Extended Reason: Hi all, I have received requests to extend the deadline. Some of the work requires revising and some of them are still on process. To be fair, I also raise my budget to compensate the time. Thanks all for your participation. Added Sunday, July 10, 2016

Target Market(s)

Construction

Industry/Entity Type

Cement

Requirements
Must have
• You will have to design two bags for two cement grades. 52.5 is of higher grade and 42.5 is of lower grade. Both are similar in design but a distinctive colours to differentiate the two at once. Please look at Reference picture 2 for ideas.
Nice to have
• You do not have to change the original logo but the Larkfield cement word font changes are required. There are no restrictions to colours and font but please refrain from using feminine colours. Instructions on rear side of the bags are now included in the scope. Please create new layout and design new user friendly symbols.
Should not have
• Since cement is a dusty product, you need avoid some colours like black as background. The dust need to be less obvious to attract attention. Our previous base colour are shown in below.
• We want a fresh look on our bag, please do not just copy our old design and make small changes. I have attached our competitors' design, please refrain from using their design as well.
• It is recommend to do some research on cement bag sector.

```html
<!DOCTYPE html>
<html lang="en">
<head>
<meta charset="utf-8">
<title>Larkfield Cement – 42.5 Bag Layout</title>
<link href="https://fonts.googleapis.com/css2?family=Exo+2:wght@600;700;800&family=Arimo:wght@400;700&display=swap" rel="stylesheet">
<style>
  :root{
    --bag:#f0d5b5;
    --ink:#231f20;
    --red:#e01b2a;
    --bg-top:#4b4b4b;
    --bg-mid:#5a5a5a;
    --bg-low:#2c2c2c;
  }
  *{box-sizing:border-box;margin:0;padding:0}
  html,body{width:1200px;height:836px;overflow:hidden}
  body{
    position:relative;
    background:linear-gradient(180deg,var(--bg-top) 0%,var(--bg-mid) 62%,var(--bg-low) 100%);
    font-family:"Exo 2",sans-serif;color:var(--ink);
  }
  .abs{position:absolute}
  .bag{position:absolute;background:var(--bag);border-radius:18px;overflow:hidden;
    box-shadow:inset 0 0 18px rgba(120,80,40,.22)}
  .gusset{position:absolute;background:var(--bag);border-radius:44px;overflow:hidden;
    box-shadow:inset 0 -8px 16px rgba(120,80,40,.22),0 4px 8px rgba(0,0,0,.25)}
  .center{left:0;right:0;text-align:center}
  .flip{transform:rotate(180deg)}
  .grade-box{position:absolute;border:2px solid var(--red);color:var(--red);text-align:center;
    font-weight:800;line-height:1}
  .grade-box .num{display:block}
  .grade-box .word{display:block;font-weight:700}
  .brand{font-weight:800;color:var(--ink);letter-spacing:1px;line-height:1}
  .edge-text{position:absolute;white-space:nowrap;font-family:"Exo 2",sans-serif;font-weight:800;color:var(--ink);transform-origin:0 0;line-height:1}
  .edge-brand{font-size:26px;letter-spacing:2px}
  .tag{border:1.5px solid var(--red);color:var(--red);font-weight:800;padding:0 5px;text-align:center}

  /* front */
  .front-title{font-size:21px;font-weight:700;line-height:27px}
  .front-class{font-size:15px;font-weight:700}
  .front-mark{font-size:54px}
  .front-sub{font-size:38px;font-weight:800;color:var(--ink);letter-spacing:1px;line-height:1}
  .dot{position:absolute;width:18px;height:18px;border-radius:50%;background:var(--red)}
  .origin{font-size:13px;font-weight:700}
  .net-label{font-size:11px;font-weight:800}
  .net-value{font-size:30px;font-weight:800}
  .net-value small{font-size:18px}

  /* back */
  .back{font-family:"Arimo",sans-serif}
  .h-small{font-size:11px;font-weight:700;letter-spacing:.3px}
  .p-small{font-size:8px}
  .mix-table{position:absolute;left:669px;top:183px;width:314px;height:112px;border:1px solid var(--ink)}
  .mix-table .col{position:absolute;top:0;bottom:0;border-left:1px solid var(--ink)}
  .mix-table .row{position:absolute;left:0;right:0;border-top:1px dashed var(--ink)}
  .mix-table .row.solid{border-top-style:solid}
  .cell-label{position:absolute;font-size:6.5px;line-height:8px}
  .buckets{position:absolute;display:flex;gap:2px}
  .bucket{width:10px;height:10px;background:var(--ink);clip-path:polygon(0 10%,100% 10%,86% 100%,14% 100%)}
  .rec{font-size:6.5px;line-height:10px}
  .rec .sq{display:inline-block;width:5px;height:5px;background:var(--ink);margin-right:6px}
  .rule{position:absolute;height:1px;background:var(--ink)}
  .icon-slot{position:absolute;width:30px;height:28px;background:#4a3d33;border-radius:3px}
  .caption{position:absolute;font-size:5.8px;line-height:7px}
  .maker-dot{position:absolute;width:24px;height:24px;border-radius:50%;background:var(--ink)}
  .maker-name{font-size:10px;font-weight:700}
  .contact{font-size:5.8px;line-height:7.2px}

  /* gussets */
  .g-quality{font-size:25px;font-weight:800;letter-spacing:.5px}
  .g-brand{font-size:48px}
  .g-weight{font-size:19px;font-weight:800}
  .g-weight small{font-size:12px}
</style>
</head>
<body>

<!-- FRONT PANEL -->
<section class="bag front" style="left:213px;top:90px;width:407px;height:477px">
  <div class="abs flip" style="left:40px;top:-8px;width:330px;display:flex;gap:10px;align-items:center">
    <span class="g-quality" style="font-size:17px">EXPORT QUALITY</span>
    <span class="tag" style="font-size:13px">42.5</span>
  </div>

  <div class="edge-text edge-brand" style="left:14px;top:150px;transform:rotate(90deg)">LARKFIELD</div>
  <div class="edge-text" style="left:22px;top:378px;transform:rotate(90deg);font-size:10px">50 Kg</div>
  <div class="edge-text" style="left:392px;top:104px;transform:rotate(-90deg);font-size:10px">50 Kg</div>
  <div class="edge-text" style="left:392px;top:60px;transform:rotate(-90deg);font-size:9px;color:var(--red)">42.5</div>
  <div class="edge-text edge-brand" style="left:393px;top:355px;transform:rotate(-90deg)">LARKFIELD</div>

  <div class="abs center front-title" style="top:40px">PORTLAND CEMENT<br>EN 197-1 (2000)</div>
  <div class="abs center front-class" style="top:100px">STRENGHT CLASS 42.5</div>

  <div class="dot" style="left:190px;top:160px"></div>
  <div class="abs" style="left:75px;right:75px;top:224px;height:4px;background:var(--ink)"></div>
  <div class="abs center brand front-mark" style="top:231px">LARKFIELD</div>
  <div class="abs" style="left:75px;right:75px;top:288px;height:4px;background:var(--ink)"></div>
  <div class="abs center front-sub" style="top:300px">CEMENT</div>

  <div class="abs origin" style="left:30px;top:396px">PRODUCT OF MYANMAR</div>
  <div class="abs net-label" style="left:301px;top:380px">NET WEIGHT</div>
  <div class="abs net-value" style="left:300px;top:390px">50 <small>Kg</small></div>

  <div class="abs" style="left:30px;top:462px;width:330px;display:flex;gap:10px;align-items:center">
    <span class="tag" style="font-size:13px">42.5</span>
    <span class="g-quality" style="font-size:17px">EXPORT QUALITY</span>
  </div>
</section>

<!-- BACK PANEL -->
<section class="bag back" style="left:625px;top:90px;width:407px;height:477px">
  <div class="abs" style="left:38px;top:-6px;width:340px;display:flex;gap:10px;align-items:center;font-family:'Exo 2',sans-serif">
    <span class="tag" style="font-size:9px;padding:0 4px;line-height:9px">42.5<br>CEMENT</span>
    <span class="g-quality" style="font-size:17px">EXPORT QUALITY</span>
  </div>

  <div class="edge-text edge-brand" style="left:14px;top:125px;transform:rotate(90deg)">LARKFIELD</div>
  <div class="edge-text edge-brand" style="left:394px;top:240px;transform:rotate(-90deg)">LARKFIELD</div>
  <div class="edge-text" style="left:397px;top:420px;transform:rotate(-90deg);font-size:9px;color:var(--red)">42.5</div>

  <div class="abs center h-small" style="top:39px">APPLICATION</div>
  <div class="abs center p-small" style="top:55px">Suitable for general concrete products.</div>
  <div class="abs center h-small" style="top:78px">MIXING INSTRUCTIONS</div>

  <div class="abs flip" style="left:40px;top:466px;width:330px;display:flex;gap:10px;align-items:center;font-family:'Exo 2',sans-serif">
    <span class="g-quality" style="font-size:17px">EXPORT QUALITY</span>
    <span class="tag" style="font-size:9px;padding:0 4px;line-height:9px">42.5<br>CEMENT</span>
  </div>
</section>

<div class="back">
  <div class="mix-table">
    <div class="col" style="left:64px"></div>
    <div class="col" style="left:122px"></div>
    <div class="col" style="left:183px"></div>
    <div class="col" style="left:265px"></div>
    <div class="row" style="top:33px"></div>
    <div class="row solid" style="top:74px"></div>
    <div class="cell-label" style="left:6px;top:17px">APPLICATIONS</div>
    <div class="cell-label" style="left:79px;top:9px">CEMENT</div>
    <div class="cell-label" style="left:143px;top:9px">SAND</div>
    <div class="cell-label" style="left:203px;top:9px">AGGREGATE</div>
    <div class="cell-label" style="left:279px;top:9px">WATER</div>
    <div class="cell-label" style="left:14px;top:48px">LEAN<br>CONCRETE</div>
    <div class="cell-label" style="left:14px;top:86px">GENERAL<br>CONCRETE</div>

    <div class="buckets" style="left:88px;top:50px"><i class="bucket"></i></div>
    <div class="buckets" style="left:129px;top:50px"><i class="bucket"></i><i class="bucket"></i><i class="bucket"></i></div>
    <div class="buckets" style="left:191px;top:50px"><i class="bucket"></i><i class="bucket"></i><i class="bucket"></i><i class="bucket"></i><i class="bucket"></i></div>
    <div class="buckets" style="left:286px;top:50px"><i class="bucket"></i></div>

    <div class="buckets" style="left:88px;top:88px"><i class="bucket"></i></div>
    <div class="buckets" style="left:135px;top:88px"><i class="bucket"></i><i class="bucket"></i></div>
    <div class="buckets" style="left:197px;top:88px"><i class="bucket"></i><i class="bucket"></i><i class="bucket"></i><i class="bucket"></i></div>
    <div class="buckets" style="left:273px;top:88px;align-items:center;font-size:5px"><i class="bucket"></i><span>OR</span><i class="bucket"></i></div>
  </div>

  <div class="abs rec" style="left:670px;top:299px;width:330px">
    <div style="font-weight:700;font-size:8px">RECOMENDATION</div>
    <div><span class="sq"></span>During 1-2 days of curing process, concrete should be sprayed with water to avoid crack</div>
    <div><span class="sq"></span>A bag of cement should be Finished with 1 day. If not, seal the bag tightly.</div>
  </div>

  <div class="rule" style="left:650px;top:348px;width:138px"></div>
  <div class="abs h-small" style="left:790px;top:341px;font-size:10px">PRECAUTION</div>
  <div class="rule" style="left:865px;top:348px;width:146px"></div>

  <div class="icon-slot" role="img" aria-label="Icon: lifting a bag with care" style="left:657px;top:362px"></div>
  <div class="icon-slot" role="img" aria-label="Icon: protective glove" style="left:724px;top:362px"></div>
  <div class="icon-slot" role="img" aria-label="Icon: dust mask" style="left:787px;top:360px"></div>
  <div class="icon-slot" role="img" aria-label="Icon: keep away from children" style="left:851px;top:362px"></div>
  <div class="icon-slot" role="img" aria-label="Icon: sun shade and raised pallet" style="left:929px;top:354px;width:48px;height:36px"></div>

  <div class="caption" style="left:652px;top:400px">Lift with care</div>
  <div class="caption" style="left:720px;top:397px;width:52px">Wear gloves while mixing or handling dry cement</div>
  <div class="caption" style="left:782px;top:397px;width:50px">Wear a mask while mixing dry cement</div>
  <div class="caption" style="left:846px;top:400px;width:60px">Keep cement away from child's reach</div>
  <div class="caption" style="left:918px;top:397px;width:90px">Store under shade and away from moisture with pallets being raised above the ground</div>

  <div class="rule" style="left:650px;top:432px;width:361px"></div>

  <div class="maker-dot" style="left:706px;top:446px"></div>
  <div class="abs contact" style="left:737px;top:448px;font-size:6.5px">Manufactured and distributed by:</div>
  <div class="abs maker-name" style="left:737px;top:458px">HARROWGATE CEMENT CO., LTD.</div>
  <div class="abs contact" style="left:702px;top:481px">No. 48, Quarry Road,<br>Between 12th and 13th Streets<br>Eastbank Township<br>Mandalay, Myanmar.</div>
  <div class="abs contact" style="left:808px;top:481px">Tel: (95)2 41100, (95)2 41101, (95)2 41102<br>&nbsp;&nbsp;&nbsp;&nbsp;&nbsp;&nbsp;&nbsp;(95)2 41103, (95)2 41104, (95)2 41105<br>Fax: (95)2 410999<br>Email: sales@harrowgatecement.example</div>
  <div class="abs contact" style="left:808px;top:515px">www.harrowgatecement.example</div>
</div>

<!-- GUSSETS -->
<section class="gusset" style="left:166px;top:568px;width:406px;height:94px">
  <div class="grade-box" style="left:45px;top:22px;width:61px;height:44px;font-size:19px;padding-top:5px">
    <span class="num">42.5</span><span class="word" style="font-size:11px;margin-top:3px">CEMENT</span>
  </div>
  <div class="abs g-quality" style="left:116px;top:28px">EXPORT QUALITY</div>
</section>

<section class="gusset" style="left:578px;top:568px;width:478px;height:94px">
  <div class="dot" style="left:80px;top:12px;width:14px;height:14px"></div>
  <div class="abs brand g-brand" style="left:52px;top:26px">LARKFIELD</div>
  <div class="abs g-weight" style="left:374px;top:14px">50 <small>Kg</small></div>
  <div class="grade-box" style="left:374px;top:47px;width:48px;height:36px;font-size:15px;padding-top:4px">
    <span class="num">42.5</span><span class="word" style="font-size:9px;margin-top:2px">CEMENT</span>
  </div>
</section>

<section class="gusset" style="left:168px;top:664px;width:477px;height:94px">
  <div class="dot" style="left:80px;top:8px;width:14px;height:14px"></div>
  <div class="abs brand g-brand" style="left:48px;top:26px">LARKFIELD</div>
  <div class="abs g-weight" style="left:368px;top:14px">50 <small>Kg</small></div>
  <div class="grade-box" style="left:368px;top:44px;width:48px;height:36px;font-size:15px;padding-top:4px">
    <span class="num">42.5</span><span class="word" style="font-size:9px;margin-top:2px">CEMENT</span>
  </div>
</section>

<section class="gusset" style="left:650px;top:664px;width:406px;height:94px">
  <div class="grade-box" style="left:46px;top:22px;width:61px;height:44px;font-size:19px;padding-top:5px">
    <span class="num">42.5</span><span class="word" style="font-size:11px;margin-top:3px">CEMENT</span>
  </div>
  <div class="abs g-quality" style="left:116px;top:28px">EXPORT QUALITY</div>
</section>

</body>
</html>
```